Real Estate Design Website

I would like to have a design for "real estate agent" website. It needs to be in a "Responsive" framework.

The design need to be suitable for different viewer from all around the world. It needs to be modern. It'd be great if there is a design for mobile and tovix/tablet (it's all under responsive framework). It needs to be easy to navigate and look modern

Target Market(s)

End user/Real estate buyers from different part of the world

Industry/Entity Type

Real Estate

Requirements
Must have
• It's for real estate agent website which is used to represent their brand/image but at the same time it also for their client which is real estate buyers
Should not have
• Should not be boring design/out of date

```html
<!DOCTYPE html>
<html lang="en">
<head>
<meta charset="utf-8">
<title>Harborline Realty</title>
<link href="https://fonts.googleapis.com/css2?family=Arimo:wght@400;700&family=Tinos&display=swap" rel="stylesheet">
<style>
:root{
  --teal:#3aa896;
  --teal-dark:#2f9683;
  --teal-deep:#197a63;
  --teal-light:#5fc8c3;
  --aqua:#6fd3d3;
  --nav-bg:#d5ead7;
  --band-light:#e6f8f6;
  --text-green:#2d8c7a;
  --body-text:#4f6a64;
  --white:#ffffff;
  --orange:#f47a20;
  --card:#3fb3a2;
  --frame:#e4f0ea;
}
*{box-sizing:border-box;margin:0;padding:0}
html,body{width:950px;height:1200px;overflow:hidden}
body{position:relative;font-family:"Arimo",Arial,sans-serif;background:var(--white);color:var(--body-text)}
.abs{position:absolute}

/* header */
.site-header{left:0;top:0;width:950px;height:83px;background:linear-gradient(90deg,#3aa896,#47b3a1 30%,#3aa896)}
.brand{left:140px;top:28px;font-family:"Tinos",serif;font-size:24px;color:var(--white)}
.brand-mark{display:inline-block;width:14px;height:14px;background:var(--white);margin-right:6px;vertical-align:1px}
.tagline{left:144px;top:55px;font-size:11px;color:#e8fbf6}
.phone{right:118px;top:52px;font-family:"Tinos",serif;font-size:18px;color:var(--white)}

.main-nav{left:0;top:83px;width:950px;height:32px;background:var(--nav-bg)}
.main-nav a{position:absolute;top:0;height:32px;line-height:34px;font-size:12px;color:var(--teal-deep);text-decoration:none}
.main-nav a.active{background:var(--teal);color:var(--white);border-radius:8px 8px 0 0;padding:0 10px;top:5px;height:27px;line-height:24px;border-bottom:3px solid var(--teal-dark)}

/* hero */
.hero{left:0;top:115px;width:950px;height:295px;background:radial-gradient(ellipse at 60% 40%,#55c3b8,#3aa896 70%)}
.slider{left:118px;top:17px;width:378px;height:253px;background:#f1f5f1;padding:7px}
.slide-photo{width:364px;height:188px;background:linear-gradient(180deg,#6fb3e6 0%,#a9d3ef 40%,#c9a55d 55%,#6e9c37 75%,#4f8a2a 100%)}
.slide-caption{width:364px;height:49px;background:var(--teal-deep);color:var(--white);padding:8px 19px}
.slide-caption h2{font-size:15px;font-weight:400}
.slide-caption p{font-size:9.5px;margin-top:4px}
.dots{left:259px;top:278px;display:flex;gap:6px}
.dots span{width:7px;height:7px;border-radius:50%;background:var(--white)}
.dots span.on{background:var(--teal-dark)}

.search-tabs{left:521px;top:16px;display:flex;gap:4px}
.search-tabs div{width:118px;height:34px;border-radius:10px 10px 0 0;font-weight:700;font-size:16px;line-height:34px;text-align:center}
.tab-on{background:var(--teal-light);color:var(--white);opacity:.55}
.tab-off{background:#a6e8e0;color:var(--teal)}
.search-panel{left:521px;top:49px;width:311px;height:246px;background:rgba(111,211,211,.45);border-radius:0 8px 0 0;color:var(--white);font-size:12px}
.search-panel .label{left:30px;top:17px}
.field{left:29px;top:42px;width:254px;height:34px;background:var(--white);border-radius:4px;border:2px solid #d8efe9;color:var(--teal);font-size:13px;line-height:30px;padding-left:13px}
.check{left:36px;top:85px;display:flex;align-items:center;gap:7px;font-size:11.5px}
.box{width:13px;height:13px;background:var(--white);border-radius:2px}
.row-label{font-size:12px}
.select{width:151px;height:24px;background:var(--white);color:var(--teal);font-size:10px;line-height:24px;padding-left:16px;border-radius:2px}
.select svg{position:absolute;right:5px;top:5px}
.search-btn{left:128px;top:195px;width:156px;height:34px;border-radius:6px;border:2px solid #c8efe9;background:linear-gradient(#6ad0c8,#3cb2a6);color:var(--white);text-align:center;line-height:30px;font-size:15px}

/* services */
.services{left:0;top:410px;width:950px;height:120px;background:linear-gradient(180deg,#f3fcfb,#bfebe4)}
.service{top:10px;width:220px}
.service h3{font-size:16px;font-weight:400;color:var(--text-green);display:flex;align-items:center;gap:6px;height:26px}
.service p{font-size:9px;line-height:16.3px;color:var(--body-text);margin-top:6px}

/* listings */
.listing{width:166px;height:149px;background:var(--card)}
.listing .photo{margin:4px;width:158px;height:101px;border:0}
.listing-frame{position:absolute;left:0;top:0;width:166px;height:108px;background:var(--frame)}
.listing .info{position:absolute;left:8px;top:112px;color:var(--white)}
.listing .info b{display:block;font-weight:400;font-size:11.5px}
.listing .info span{display:block;font-size:10px;margin-top:3px}
.listing svg{position:absolute;right:9px;top:118px}

/* members */
.members{left:0;top:883px;width:950px;height:146px;background:var(--teal)}
.member-box{top:10px;height:82px;border:1px solid #8ddbd3;border-radius:4px;background:rgba(111,211,211,.55)}
.member-box h4{position:absolute;left:18px;top:9px;font-weight:400;font-size:17px;color:var(--white)}
.input{position:absolute;top:40px;height:24px;background:var(--white);color:var(--teal);font-size:12px;line-height:24px;padding-left:8px}
.btn{position:absolute;top:39px;height:26px;border:2px solid #d0f0ea;border-radius:5px;background:var(--teal);color:var(--white);font-size:12px;text-align:center;line-height:22px}
.signup{left:118px;top:100px;width:351px;height:36px;border-radius:4px;background:linear-gradient(90deg,#7ad8d4,#5cc8c3);overflow:hidden}
.signup .ask{position:absolute;left:36px;top:9px;color:var(--white);font-size:16px}
.signup .go{position:absolute;right:0;top:0;width:130px;height:36px;background:var(--orange);clip-path:polygon(10% 0,100% 0,100% 100%,0 100%,10% 100%,0 100%);color:var(--white);font-size:16px;line-height:36px;padding-left:24px}
.social{top:101px;width:34px;height:34px;border-radius:3px}

/* footer */
.site-footer{left:0;top:1029px;width:950px;height:171px;background:var(--teal-dark);color:#d7f1ea}
.site-footer h5{font-size:12px;font-weight:700;color:var(--white);margin-bottom:13px}
.site-footer ul{list-style:none;font-size:9.5px;line-height:16.3px;letter-spacing:.4px}
.testimonial{font-size:9.5px;line-height:16.3px;letter-spacing:.2px}
.testimonial strong{color:var(--white);display:block}
.foot-brand{left:658px;top:22px;font-family:"Tinos",serif;font-size:15px;color:var(--white)}
.arrows{display:inline-flex;gap:4px;vertical-align:-2px;margin-left:10px}
.arrows i{width:12px;height:12px;border-radius:50%;background:#6cc1b2;display:inline-block}
</style>
</head>
<body>

<header class="abs site-header">
  <div class="abs brand"><span class="brand-mark"></span>Harborline Realty</div>
  <div class="abs tagline">Lorem Ipsum is simply dummy text</div>
  <div class="abs phone">Call us: (555) 014-2280</div>
</header>

<nav class="abs main-nav">
  <a href="#" style="left:134px">Home</a>
  <a href="#" class="active" style="left:189px">Our Story</a>
  <a href="#" style="left:283px">Tenant</a>
  <a href="#" style="left:353px">Owner</a>
  <a href="#" style="left:422px">Buying</a>
  <a href="#" style="left:491px">Contact us</a>
</nav>

<section class="abs hero">
  <div class="abs slider">
    <div class="slide-photo" role="img" aria-label="Photo of a two-storey house on a lawn with a for-sale sign"></div>
    <div class="slide-caption">
      <h2>Lorem Ipsum is simply dummy text of</h2>
      <p>We work with investors to make managing your investments easy!</p>
    </div>
  </div>
  <div class="abs dots"><span></span><span></span><span class="on"></span><span></span><span></span></div>

  <div class="abs search-tabs"><div class="tab-on" style="opacity:1;background:rgba(111,211,211,.45)">Tenants</div><div class="tab-off">Oweners</div></div>
  <div class="abs search-panel">
    <div class="abs label">Address, Suburbs, Postcodes, or Regions</div>
    <div class="abs field">Example: Cedarbrook Falls, Texas 70000</div>
    <div class="abs check"><span class="box"><svg width="13" height="13"><path d="M3 6.5l2.5 2.5 4.5-5" stroke="#3aa896" stroke-width="2" fill="none"/></svg></span>Include surrounding suburbs</div>
    <div class="abs row-label" style="left:34px;top:122px">Property Type :</div>
    <div class="abs select" style="left:131px;top:114px">Select one<svg width="10" height="14"><path d="M1 6l4-5 4 5zM1 8l4 5 4-5z" fill="#555"/></svg></div>
    <div class="abs row-label" style="left:53px;top:159px">Bedrooms :</div>
    <div class="abs select" style="left:131px;top:152px">Select one<svg width="10" height="14"><path d="M1 6l4-5 4 5zM1 8l4 5 4-5z" fill="#555"/></svg></div>
    <div class="abs search-btn">Search</div>
  </div>
</section>

<section class="abs services">
  <div class="abs service" style="left:119px">
    <h3><svg width="22" height="20"><path d="M11 1L1 10h3v9h14v-9h3z" fill="#3aa896"/></svg>Buy a home</h3>
    <p>Lorem Ipsum is simply dummy text of the printing and typesetting industry. Lorem Ipsum has been the industry's standard dummy text ever since the 1500s, when an unknown</p>
  </div>
  <div class="abs service" style="left:368px">
    <h3><svg width="22" height="20"><path d="M11 1L1 10h3v9h14v-9h3z" fill="#3aa896"/></svg>Sell a home</h3>
    <p>Lorem Ipsum is simply dummy text of the printing and typesetting industry. Lorem Ipsum has been the industry's standard dummy text ever since the 1500s, when an</p>
  </div>
  <div class="abs service" style="left:618px;width:222px">
    <h3><svg width="22" height="20"><path d="M11 1L1 10h3v9h14v-9h3z" fill="#3aa896"/></svg>Rent a home</h3>
    <p>Lorem Ipsum is simply dummy text of the printing and typesetting industry. Lorem Ipsum has been the industry's standard dummy text ever since the 1500s, when an unknown printer took</p>
  </div>
</section>

<!-- listings -->
<div class="abs listing" style="left:118px;top:546px"><div class="listing-frame"></div><div class="abs photo" role="img" aria-label="Photo of a mid-rise apartment resort with a pool" style="background:linear-gradient(#9ec3e6,#c98f6f 55%,#6f9a5a)"></div><div class="info"><b>Lorem ipsum dolor sit</b><span>Ut enim ad minim</span></div><svg width="26" height="22"><circle cx="9" cy="9" r="6.5" stroke="#fff" stroke-width="2.5" fill="none"/><path d="M14 13l9 7" stroke="#fff" stroke-width="4" stroke-linecap="round"/></svg></div>
<div class="abs listing" style="left:302px;top:546px"><div class="listing-frame"></div><div class="abs photo" role="img" aria-label="Illustration of a modern villa with green roofs" style="background:linear-gradient(#5a7d8e,#d5d6cf 55%,#5f9a3e)"></div><div class="info"><b>Lorem ipsum dolor sit</b><span>Ut enim ad minim</span></div><svg width="26" height="22"><circle cx="9" cy="9" r="6.5" stroke="#fff" stroke-width="2.5" fill="none"/><path d="M14 13l9 7" stroke="#fff" stroke-width="4" stroke-linecap="round"/></svg></div>
<div class="abs listing" style="left:484px;top:546px"><div class="listing-frame"></div><div class="abs photo" role="img" aria-label="Illustration of colourful high-rise residential towers" style="background:linear-gradient(#c6dcef,#6fb7a0 50%,#b7463a 85%,#7aa35a)"></div><div class="info"><b>Lorem ipsum dolor sit</b><span>Ut enim ad minim</span></div><svg width="26" height="22"><circle cx="9" cy="9" r="6.5" stroke="#fff" stroke-width="2.5" fill="none"/><path d="M14 13l9 7" stroke="#fff" stroke-width="4" stroke-linecap="round"/></svg></div>
<div class="abs listing" style="left:666px;top:546px"><div class="listing-frame"></div><div class="abs photo" role="img" aria-label="Photo of green countryside land under a blue sky" style="background:linear-gradient(#2d6fc4,#a8d0ef 50%,#5fae2f 70%,#3d8a1f)"></div><div class="info"><b>Lorem ipsum dolor sit</b><span>Ut enim ad minim</span></div><svg width="26" height="22"><circle cx="9" cy="9" r="6.5" stroke="#fff" stroke-width="2.5" fill="none"/><path d="M14 13l9 7" stroke="#fff" stroke-width="4" stroke-linecap="round"/></svg></div>

<div class="abs listing" style="left:118px;top:714px"><div class="listing-frame"></div><div class="abs photo" role="img" aria-label="Photo of cream townhouses with green roofs" style="background:linear-gradient(#8fbbe0,#e6dca8 45%,#6f8c50 85%)"></div><div class="info"><b>Lorem ipsum dolor sit</b><span>Ut enim ad minim</span></div><svg width="26" height="22"><circle cx="9" cy="9" r="6.5" stroke="#fff" stroke-width="2.5" fill="none"/><path d="M14 13l9 7" stroke="#fff" stroke-width="4" stroke-linecap="round"/></svg></div>
<div class="abs listing" style="left:302px;top:714px"><div class="listing-frame"></div><div class="abs photo" role="img" aria-label="Illustration of white apartment towers among palms" style="background:linear-gradient(#2a4fa0,#cfd6e0 45%,#4a7a3a)"></div><div class="info"><b>Lorem ipsum dolor sit</b><span>Ut enim ad minim</span></div><svg width="26" height="22"><circle cx="9" cy="9" r="6.5" stroke="#fff" stroke-width="2.5" fill="none"/><path d="M14 13l9 7" stroke="#fff" stroke-width="4" stroke-linecap="round"/></svg></div>
<div class="abs listing" style="left:484px;top:714px"><div class="listing-frame"></div><div class="abs photo" role="img" aria-label="Photo of a family house on a wide lawn" style="background:linear-gradient(#9cc4e8,#c9d4d4 40%,#5d8a3c 60%,#7fb04a)"></div><div class="info"><b>Lorem ipsum dolor sit</b><span>Ut enim ad minim</span></div><svg width="26" height="22"><circle cx="9" cy="9" r="6.5" stroke="#fff" stroke-width="2.5" fill="none"/><path d="M14 13l9 7" stroke="#fff" stroke-width="4" stroke-linecap="round"/></svg></div>
<div class="abs listing" style="left:666px;top:714px"><div class="listing-frame"></div><div class="abs photo" role="img" aria-label="Illustration of residential towers beside a landscaped park" style="background:linear-gradient(#4a86c8,#dfe3d8 45%,#4e9a45 80%)"></div><div class="info"><b>Lorem ipsum dolor sit</b><span>Ut enim ad minim</span></div><svg width="26" height="22"><circle cx="9" cy="9" r="6.5" stroke="#fff" stroke-width="2.5" fill="none"/><path d="M14 13l9 7" stroke="#fff" stroke-width="4" stroke-linecap="round"/></svg></div>

<section class="abs members">
  <div class="abs member-box" style="left:118px;width:351px">
    <h4>Member login</h4>
    <div class="input" style="left:18px;width:112px">User name</div>
    <div class="input" style="left:143px;width:112px">Password</div>
    <div class="btn" style="left:264px;width:70px">Login</div>
  </div>
  <div class="abs member-box" style="left:481px;width:351px">
    <h4 style="font-size:15px;top:11px">Subscribe to our weekly newsletter</h4>
    <div class="input" style="left:16px;width:231px">email address</div>
    <div class="btn" style="left:254px;width:81px">Subscribe</div>
  </div>
  <div class="abs signup"><span class="ask">Not a member yet</span><span class="go">Signup Now</span></div>
  <div class="abs social" style="left:483px;background:#3f6bb5"></div>
  <div class="abs social" style="left:530px;background:#3fb7e8"></div>
  <div class="abs social" style="left:578px;background:#333"></div>
</section>

<footer class="abs site-footer">
  <div class="abs" style="left:126px;top:23px">
    <h5>About Us</h5>
    <ul><li>About us</li><li>Why us</li><li>Customer Stories</li><li>Press Resources</li><li>Press Releases</li><li>Contact us</li></ul>
  </div>
  <div class="abs" style="left:266px;top:23px">
    <h5>Proparties</h5>
    <ul><li>Rent a home</li><li>Lease a home</li><li>Buy a home</li><li>Sell a home</li><li>Ask advices</li></ul>
  </div>
  <div class="abs" style="left:408px;top:23px;width:240px">
    <h5>Costamer Testimonials<span class="arrows"><i></i><i></i></span></h5>
    <p class="testimonial">Lorem Ipsum is simply dummy text of the printing and typesetting industry. Lorem Ipsum has been the industr standard dummy text ever since the 1500s, when an unknown printer took a<strong>Lorem Ipsum is simply</strong><strong>Owner, Lorem Ipsum</strong></p>
  </div>
  <div class="abs foot-brand"><span class="brand-mark" style="width:11px;height:11px"></span>Harborline Realty</div>
</footer>

</body>
</html>
```